Stationary for 2-office law firm with global theme

I need stationary with contact info for two offices. I'd like the same letterhead design to work for printing on stationary and also for digital use in Word. The colors and feel should match the new logo, which is a stylized globe with and "F" in it. I'd also like envelopes with an eye-catching design.

Target Market(s)

U.S. citizens seeking dual citizenship with Italy or Ireland

Industry/Entity Type

Law

Font styles to use
Serif
Sans Serif
Other font styles liked:
• To match the logo?

Colors
0054AA
0677BA
7BADD7
CADEEF
E8F1F8

Requirements
Must have
• Clean, modern design incorporating new logo

```html
<!DOCTYPE html>
<html lang="en">
<head>
<meta charset="utf-8">
<title>Vantoria Law — Stationery Set</title>
<link href="https://fonts.googleapis.com/css2?family=Lato:wght@400;700;900&display=swap" rel="stylesheet">
<style>
  :root {
    --navy: #153c6b;
    --sky: #29abe2;
    --ink: #2b2b2b;
    --paper: #ffffff;
    --backdrop: #ebe8e2;
    --faint: #eef3f9;
    --rule: #b9b9b9;
  }
  * { box-sizing: border-box; margin: 0; padding: 0; }
  html, body { width: 1200px; height: 1200px; overflow: hidden; }
  body {
    position: relative;
    background: var(--backdrop);
    font-family: "Lato", Arial, sans-serif;
    color: var(--ink);
  }
  .sheet {
    position: absolute;
    background: var(--paper);
    overflow: hidden;
    box-shadow: 0 3px 10px rgba(0,0,0,0.18);
  }
  .wave { position: absolute; left: 0; bottom: 0; width: 100%; display: block; }
  .brand-mark { position: absolute; border-radius: 50%; background: var(--sky); }
  .brand-name {
    position: absolute;
    font-weight: 900;
    color: var(--navy);
    letter-spacing: 0.01em;
    line-height: 1;
    white-space: nowrap;
  }
  .contact-block { position: absolute; border-left: 2px solid var(--sky); }
  .contact-line { display: flex; align-items: center; white-space: nowrap; }
  .contact-line svg { flex: none; }

  /* Letterhead */
  .letterhead { left: 19px; top: 110px; width: 731px; height: 940px; }
  .letterhead .brand-mark { left: 60px; top: 56px; width: 78px; height: 78px; }
  .letterhead .brand-name { left: 159px; top: 82px; font-size: 31px; }
  .letterhead .backdrop-mark {
    position: absolute; left: 146px; top: 279px; width: 448px; height: 448px;
    border-radius: 50%; background: var(--faint);
  }
  .letterhead .contact-block { left: 509px; top: 54px; height: 84px; padding-left: 18px; font-size: 12px; line-height: 14px; }
  .letterhead .contact-line { gap: 6px; }
  .letterhead .address { margin-bottom: 6px; }

  /* Envelope front */
  .envelope-front { left: 783px; top: 110px; width: 356px; height: 154px; }
  .envelope-front .brand-mark { left: 23px; top: 17px; width: 34px; height: 34px; }
  .envelope-front .brand-name { left: 67px; top: 27px; font-size: 15px; }
  .envelope-front .contact-block { left: 23px; top: 72px; padding-left: 5px; font-size: 5.5px; line-height: 8px; border-left-width: 1px; }

  /* Envelope back */
  .envelope-back { left: 783px; top: 309px; width: 356px; height: 153px; }
  .envelope-back .flap-text { position: absolute; left: 0; top: 16px; width: 100%; text-align: center; font-weight: 900; font-size: 10px; color: var(--paper); letter-spacing: 0.04em; }

  /* Business card front */
  .card-front { left: 783px; top: 602px; width: 357px; height: 206px; }
  .card-front .brand-mark { left: 69px; top: 56px; width: 52px; height: 52px; }
  .card-front .brand-name { left: 0; width: 179px; text-align: center; top: 117px; font-size: 19px; line-height: 20px; }
  .card-front .contact-block { left: 179px; top: 57px; height: 93px; padding-left: 18px; font-size: 9px; line-height: 12px; border-left-width: 1px; }
  .card-front .person { font-size: 11px; font-weight: 900; color: var(--navy); letter-spacing: 0.02em; line-height: 13px; }
  .card-front .person span { color: var(--sky); }
  .card-front .role { margin-bottom: 5px; }
  .card-front .address { margin-bottom: 5px; }
  .card-front .contact-line { gap: 4px; }

  /* Business card back */
  .card-back { left: 783px; top: 843px; width: 357px; height: 206px; background: var(--navy); }
  .card-back .brand-mark { left: 148px; top: 44px; width: 62px; height: 62px; }
  .card-back .brand-name { left: 0; width: 100%; text-align: center; top: 117px; font-size: 24px; line-height: 25px; color: var(--paper); }
</style>
</head>
<body>

<!-- Letterhead -->
<section class="sheet letterhead">
  <div class="backdrop-mark"></div>
  <div class="brand-mark"></div>
  <div class="brand-name">VANTORIA LAW</div>
  <div class="contact-block">
    <p class="address">18 Linden Avenue, Oakmere<br>NC 274, United States</p>
    <p class="contact-line"><svg width="9" height="9" viewBox="0 0 10 10"><path d="M2 1 L4 1 L4.6 3 L3.4 4 C4 5.6 4.6 6.2 6 6.6 L7 5.4 L9 6 L9 8 C5 9 1 5 2 1Z" fill="var(--sky)"/></svg>000-000-000-000</p>
    <p class="contact-line"><svg width="9" height="10" viewBox="0 0 8 10"><rect x="1.5" y="0.5" width="5" height="9" rx="1" fill="none" stroke="var(--sky)"/></svg>000-000-000-000</p>
    <p class="contact-line"><svg width="9" height="9" viewBox="0 0 10 8"><rect x="0.5" y="0.5" width="9" height="7" fill="var(--sky)"/><path d="M0.5 0.5 L5 4.5 L9.5 0.5" fill="none" stroke="#fff"/></svg>info@vantorialaw.com</p>
    <p class="contact-line"><svg width="9" height="9" viewBox="0 0 10 10"><circle cx="5" cy="5" r="4.3" fill="none" stroke="var(--sky)"/><path d="M0.7 5 H9.3 M5 0.7 C2.5 3 2.5 7 5 9.3 M5 0.7 C7.5 3 7.5 7 5 9.3" fill="none" stroke="var(--sky)" stroke-width="0.8"/></svg>www.vantorialaw.com</p>
  </div>
  <svg class="wave" viewBox="0 0 731 120" preserveAspectRatio="none" height="120">
    <path d="M250,86 C420,92 600,70 731,12 L731,42 C600,86 420,96 250,86Z" fill="var(--sky)"/>
    <path d="M0,13 C180,70 380,100 520,96 C620,92 690,70 731,48 L731,120 L0,120Z" fill="var(--navy)"/>
  </svg>
</section>

<!-- Envelope front -->
<section class="sheet envelope-front">
  <div class="brand-mark"></div>
  <div class="brand-name">VANTORIA LAW</div>
  <div class="contact-block">
    <p>2140 Linden Avenue, Oakmere</p>
    <p>NC 27410, United States</p>
  </div>
  <svg class="wave" viewBox="0 0 356 44" preserveAspectRatio="none" height="44">
    <path d="M105,30 C200,34 290,26 356,0 L356,12 C290,32 200,36 105,30Z" fill="var(--sky)"/>
    <path d="M0,2 C90,25 190,36 260,34 C305,32 335,24 356,16 L356,44 L0,44Z" fill="var(--navy)"/>
  </svg>
</section>

<!-- Envelope back -->
<section class="sheet envelope-back">
  <svg width="356" height="153" viewBox="0 0 356 153" style="position:absolute;left:0;top:0">
    <path d="M8,45 L1,153 M348,45 L355,153" stroke="var(--rule)" stroke-width="0.8" fill="none"/>
    <path d="M0,0 L356,0 L356,28 L350,40 C348,44 346,45 342,45 L14,45 C10,45 8,44 6,40 L0,28Z" fill="var(--navy)"/>
  </svg>
  <div class="flap-text">VANTORIA LAW</div>
</section>

<!-- Business card front -->
<section class="sheet card-front">
  <div class="brand-mark"></div>
  <div class="brand-name">VANTORIA<br>LAW</div>
  <div class="contact-block">
    <p class="person">DANIEL <span>HARPER</span></p>
    <p class="role">President</p>
    <p class="address">2140 Linden Avenue, Oakmere<br>NC 27410, United States</p>
    <p class="contact-line"><svg width="7" height="7" viewBox="0 0 10 10"><path d="M2 1 L4 1 L4.6 3 L3.4 4 C4 5.6 4.6 6.2 6 6.6 L7 5.4 L9 6 L9 8 C5 9 1 5 2 1Z" fill="var(--sky)"/></svg>000-000-000-000</p>
    <p class="contact-line"><svg width="7" height="7" viewBox="0 0 10 8"><rect x="0.5" y="0.5" width="9" height="7" fill="var(--sky)"/><path d="M0.5 0.5 L5 4.5 L9.5 0.5" fill="none" stroke="#fff"/></svg>info@vantorialaw.com</p>
    <p class="contact-line"><svg width="7" height="7" viewBox="0 0 10 10"><circle cx="5" cy="5" r="4.3" fill="none" stroke="var(--sky)"/><path d="M0.7 5 H9.3 M5 0.7 C2.5 3 2.5 7 5 9.3 M5 0.7 C7.5 3 7.5 7 5 9.3" fill="none" stroke="var(--sky)" stroke-width="0.8"/></svg>www.vantorialaw.com</p>
  </div>
  <svg class="wave" viewBox="0 0 357 42" preserveAspectRatio="none" height="42">
    <path d="M200,28 C270,26 320,14 357,0 L357,10 C320,22 270,30 200,28Z" fill="var(--sky)"/>
    <path d="M0,2 C80,22 170,30 240,28 C290,26 330,18 357,12 L357,42 L0,42Z" fill="var(--navy)"/>
  </svg>
</section>

<!-- Business card back -->
<section class="sheet card-back">
  <div class="brand-mark"></div>
  <div class="brand-name">VANTORIA LAW</div>
  <svg class="wave" viewBox="0 0 357 42" preserveAspectRatio="none" height="42">
    <path d="M0,0 C80,24 170,34 240,32 C290,30 330,22 357,14 L357,42 L0,42Z" fill="var(--paper)"/>
    <path d="M200,30 C270,28 320,16 357,2 L357,12 C320,24 270,32 200,30Z" fill="var(--sky)"/>
  </svg>
</section>

</body>
</html>
```